Business Card Design for Online Gift Business

Business card design for a new online Canadian company called "Hale & Brook Gift Boxes" selling modern and luxurious gift boxes for every occasion. Items are sourced locally from talented socially-responsible Canadian artisans. Each gift is elegantly presented in a keepsake wood box to ensure a lasting impression.

Industry/Entity Type

E-Commerce

Contact Information for Business Card

Marla Pendleton, Proprietor
Brookvale, AB
403-555-2741
www.haleandbrook.ca
hello@haleandbrook.ca

Requirements
Must have
• Gifts from our hands, to your heart
• Please also include the symbols for Facepage and snapgram
Nice to have
• **I have attached a few samples of background colors and font colors that I like. I hope this helps in a few directions to try.

```html
<!DOCTYPE html>
<html lang="en">
<head>
<meta charset="utf-8">
<title>Hale &amp; Brook Gift Boxes – Business Card</title>
<link rel="stylesheet" href="https://fonts.googleapis.com/css2?family=Cinzel:wght@400&family=Great+Vibes&family=Ubuntu:wght@400;500&display=swap">
<style>
  :root {
    --backdrop: #8e8e8e;
    --ink: #000000;
    --gold: #b09b74;
    --tan: #b59e7a;
    --white: #ffffff;
    --blue: #3a62b5;
    --sky: #4aa3dc;
    --green: #5bb84a;
    --violet: #5a45a0;
    --navy: #24226a;
    --pink: #e0407a;
    --red: #e8313e;
    --orange: #f07a2a;
    --yellow: #ecc23a;
    --cyan: #55c6e6;
  }
  html, body {
    margin: 0;
    padding: 0;
    width: 980px;
    height: 1200px;
    overflow: hidden;
    background: var(--backdrop);
  }
  .canvas {
    position: relative;
    width: 980px;
    height: 1200px;
  }
  .card {
    position: absolute;
    display: block;
  }
  .card--front { left: 126px; top: 131px; }
  .card--back { left: 119px; top: 710px; }
  .brand-name {
    font-family: "Cinzel", serif;
    font-weight: 400;
    fill: var(--gold);
  }
  .tagline {
    font-family: "Great Vibes", cursive;
    fill: var(--gold);
  }
  .person-name {
    font-family: "Ubuntu", sans-serif;
    font-weight: 500;
    font-size: 34px;
    fill: var(--white);
  }
  .person-role, .contact-text, .social-text {
    font-family: "Ubuntu", sans-serif;
    font-weight: 400;
    fill: var(--white);
  }
  .person-role { font-size: 23px; }
  .contact-text { font-size: 19px; }
  .contact-text--phone { font-size: 24px; }
  .contact-text--place { font-size: 21px; }
  .social-text { font-size: 18px; }
  .icon { fill: none; stroke: var(--white); stroke-width: 2; stroke-linecap: round; stroke-linejoin: round; }
  .icon-solid { fill: var(--white); }
</style>
</head>
<body>
<main class="canvas">

  <svg class="card card--front" width="714" height="410" viewBox="0 0 714 410" xmlns="http://www.w3.org/2000/svg">
    <defs>
      <linearGradient id="front-upper" x1="0" y1="0" x2="1" y2="0.3">
        <stop offset="0" stop-color="var(--blue)"/>
        <stop offset="0.25" stop-color="var(--sky)"/>
        <stop offset="0.4" stop-color="var(--green)"/>
        <stop offset="0.55" stop-color="var(--blue)"/>
        <stop offset="0.7" stop-color="var(--pink)"/>
        <stop offset="0.85" stop-color="var(--violet)"/>
        <stop offset="1" stop-color="var(--navy)"/>
      </linearGradient>
      <linearGradient id="front-lower" x1="0" y1="0" x2="1" y2="0">
        <stop offset="0" stop-color="var(--blue)"/>
        <stop offset="0.15" stop-color="var(--red)"/>
        <stop offset="0.4" stop-color="var(--orange)"/>
        <stop offset="0.6" stop-color="var(--yellow)"/>
        <stop offset="0.78" stop-color="var(--cyan)"/>
        <stop offset="1" stop-color="var(--sky)"/>
      </linearGradient>
    </defs>
    <rect class="pattern" role="img" aria-label="Colourful low-poly geometric pattern" x="0" y="0" width="714" height="211" fill="url(#front-upper)"/>
    <rect class="pattern" role="img" aria-label="Colourful low-poly geometric pattern" x="0" y="309" width="714" height="101" fill="url(#front-lower)"/>
    <rect class="band" x="0" y="211" width="714" height="98" fill="var(--ink)"/>
    <polygon class="band-tab" points="162,212 162,143 354,106 552,143 552,212" fill="var(--ink)"/>
    <text class="brand-name" x="354" y="213" font-size="44" text-anchor="middle">Hale &amp; Brook</text>
    <text class="tagline" x="354" y="276" font-size="28" text-anchor="middle">Gifts from our hands, to your heart</text>
  </svg>

  <svg class="card card--back" width="714" height="413" viewBox="0 0 714 413" xmlns="http://www.w3.org/2000/svg">
    <defs>
      <linearGradient id="back-upper" x1="0" y1="0" x2="1" y2="0">
        <stop offset="0" stop-color="var(--sky)"/>
        <stop offset="0.2" stop-color="var(--cyan)"/>
        <stop offset="0.35" stop-color="var(--green)"/>
        <stop offset="0.55" stop-color="var(--orange)"/>
        <stop offset="0.7" stop-color="var(--yellow)"/>
        <stop offset="0.85" stop-color="var(--pink)"/>
        <stop offset="1" stop-color="var(--violet)"/>
      </linearGradient>
    </defs>
    <rect class="tan-panel" x="0" y="0" width="714" height="413" fill="var(--tan)"/>
    <rect class="pattern" role="img" aria-label="Colourful low-poly geometric pattern" x="0" y="0" width="714" height="94" fill="url(#back-upper)"/>
    <rect class="band" x="0" y="94" width="714" height="77" fill="var(--ink)"/>
    <polygon class="band-badge" points="238,91 355,52 472,91 472,171 355,211 238,171" fill="var(--ink)"/>
    <text class="brand-name" x="355" y="145" font-size="36" text-anchor="middle">Hale &amp; Brook</text>

    <text class="person-name" x="172" y="278" text-anchor="middle">Marla Pendleton</text>
    <text class="person-role" x="172" y="311" text-anchor="middle">Proprietor</text>

    <circle class="icon-solid" cx="23" cy="358" r="11"/>
    <text class="social-text" x="48" y="364">Facepage</text>
    <circle class="icon-solid" cx="23" cy="387" r="11"/>
    <text class="social-text" x="48" y="393">snapgram</text>

    <rect class="divider" x="344" y="224" width="4" height="163" fill="var(--white)"/>

    <path class="icon-solid" d="M378 251 l5 -2 l4 7 l-3 3 q2 5 7 7 l3 -3 l7 4 l-2 5 q-12 1 -21 -21 z"/>
    <text class="contact-text contact-text--phone" x="435" y="269">403-555-2741</text>

    <g class="icon">
      <rect x="373" y="287" width="24" height="16"/>
      <path d="M373 287 l12 9 l12 -9"/>
      <path d="M373 303 l9 -7 M397 303 l-9 -7"/>
    </g>
    <text class="contact-text" x="434" y="302">hello@haleandbrook.ca</text>

    <g class="icon">
      <circle cx="384" cy="332" r="12"/>
      <ellipse cx="384" cy="332" rx="5" ry="12"/>
      <path d="M372 332 h24 M374 326 h20 M374 338 h20"/>
    </g>
    <text class="contact-text" x="436" y="339">www.haleandbrook.ca</text>

    <g class="icon">
      <path d="M393 378 q-8 -9 -8 -14 a8 8 0 0 1 16 0 q0 5 -8 14 z"/>
      <circle cx="393" cy="364" r="3"/>
    </g>
    <path class="icon-solid" d="M367 384 l6 -10 h9 l-3 10 z M382 384 l3 -10 h3 l4 10 z"/>
    <text class="contact-text contact-text--place" x="436" y="377">Brookvale, AB</text>
  </svg>

</main>
</body>
</html>
```